Lirra Dusk a young drag queen needs a website to promote herself

URLs: queenlirra.example / lirradusk.example
General Requests
• SEO-Optimized
• CMS: Joomla
Lirra Dusk is a young Drag queen still going to college and living in the us. She has an international Background with Canadian and Swiss citizenship. She is very creative not only in her Shows but she is also a painter, a Fashion designer a Music writer, a singer and an excellent vegan cook.

In order to promote her and to book her for a Show or a maquillage she needs a Website that will highly interact with social Media.

The Structure of the Website could be as follows:

Welcome page
From the Welcome page navigation to
1. Blog
a. Easy tool to add new Blogs
b. Possibility for others to write comments
c. Possibilty to
2. Events: Videos and Pictures
a. Easy Way to Ad Pictures and Vidoes and Showing a Title/Description
3. Upcoming Events and Shows
a. Possibility to describe Upcoming shows with link for more Information and Registration
4. Book a Show
a. I offer a lot of different Shows with Dancing, Singing or Moderating an Evening. Since I Speak English, (Swiss-)German and French I can entertain a multicultural Audience. Just get in touch with me and let’s discuss it.
b. Contact form for ordering an offer for a show (Name and Address; Kind of Show, Duration, Date, Place, Budget, Captcha)
c. lirra@lirradusk.example
5. Book a Maquillage
a. Do you want to look like a Drag? Are you a young Drag and want to learn how to get dressed up an a unique Maquillage? Do you want to have a special surprise for a Bachelors Party? Just ask me! I’m your Expert! Also available as Gift Certificate.
b. Contact form for ordering an offer for a Maquillage (Name and Address; Kind of Maquillage, Option for Gift Certificate; Occasion, Date, Place, Budget; captcha);
c. Form mailed to lirra@lirradusk.example
6. Lirra on Social Media
a. Join me on Fanpage
b. Join me on Snapgrid
c. Join me on Tunewave
7. Sponsors and Partners
a. Banner Glow Mesa
b. ….
Updates

Industry/Entity Type

College

Number of Pages Required

5+ page

Font styles to use
Decorative

Colors
6b449b
d2a4cc
e4daeb

Requirements
Must have
• Responsive Design

```html
<!DOCTYPE html>
<html lang="en">
<head>
<meta charset="utf-8">
<title>Lirra Dusk – Drag Queen</title>
<link href="https://fonts.googleapis.com/css2?family=Rye&family=Playfair+Display:wght@400;700&family=Open+Sans:wght@400;600;700&display=swap" rel="stylesheet">
<style>
:root{
  --ink:#0d0d0d;
  --night:#141414;
  --smoke:#232323;
  --ash:#3a3a3a;
  --gold:#e9c79c;
  --gold-deep:#c9a26f;
  --text:#d8d3cc;
  --muted:#9b958e;
  --white:#ffffff;
  --violet:#6b449b;
  --orchid:#d2a4cc;
  --lilac:#e4daeb;
  --fan:#3b5a9a;
  --tune:#f26f22;
  --snap:#2f7bbf;
}
*{box-sizing:border-box;margin:0;padding:0}
html,body{width:1200px;height:2684px;overflow:hidden;background:var(--ink)}
body{position:relative;font-family:"Open Sans",Arial,sans-serif;color:var(--text)}
.abs{position:absolute}
.logo{font-family:"Playfair Display",Georgia,serif;color:var(--white);font-weight:400}
.social-dots{display:flex;gap:10px}
.social-dots span{width:30px;height:30px;border:2px solid var(--white);border-radius:50%;display:block}
.site-header{left:0;top:0;width:1200px;height:72px;background:var(--night)}
.site-header .logo{left:52px;top:10px;font-size:42px}
.site-header .social-dots{right:52px;top:21px;position:absolute}
.main-nav{left:0;top:72px;width:1200px;height:48px;background:#090909;border-top:1px solid #2a2a2a;border-bottom:1px solid #2a2a2a;display:flex;align-items:center;padding-left:64px;gap:34px}
.main-nav a{color:var(--white);font-size:12px;text-transform:uppercase;letter-spacing:.5px;text-decoration:none}
.hero{left:0;top:120px;width:1200px;height:570px;background:radial-gradient(ellipse at 55% 50%,#2b2b2b,#0e0e0e 70%)}
.photo{display:block}
.hero-left{left:40px;top:0;width:360px;height:570px;background:radial-gradient(ellipse at 55% 40%,#6d6a66,#2a2826 55%,#0e0e0e 85%)}
.hero-right{left:790px;top:0;width:410px;height:570px;background:linear-gradient(160deg,#bcd8ef,#6fa6d4 45%,#e6eef5 100%)}
.hero-title{left:580px;top:232px;font-family:"Rye",serif;font-size:62px;color:var(--gold);letter-spacing:2px}
.hero-copy{left:584px;top:318px;width:200px;font-size:13px;line-height:1.6;color:var(--text)}
.btn{display:inline-block;border:2px solid var(--white);color:var(--white);background:#000;font-size:12px;font-weight:700;text-transform:uppercase;letter-spacing:.6px;padding:9px 16px}
.hero .btn{left:584px;top:438px;position:absolute}
.slider-ctrl{left:120px;top:536px}
.about{left:0;top:690px;width:1200px;height:420px;background:linear-gradient(180deg,#1c1c1c,#262626 60%,#1a1a1a)}
.section-title{font-family:"Rye",serif;color:var(--gold);text-transform:uppercase;font-weight:400}
.about .section-title{left:72px;top:40px;font-size:50px}
.about-copy{left:72px;top:118px;width:520px;font-size:14px;line-height:1.85;color:var(--text)}
.about .btn{left:72px;top:354px;position:absolute}
.about-photo{left:640px;top:560px;width:380px;height:540px;background:radial-gradient(ellipse at 50% 38%,#d9d6d2,#585450 40%,#1c1c1c 78%);border-radius:46% 46% 0 0;z-index:2}
.feeds{left:0;top:1110px;width:1200px;height:480px;background:var(--night)}
.feeds .section-title{font-size:30px;top:10px}
.img-block{position:absolute}
.play{left:230px;top:62px;width:64px;height:64px}
.post{position:absolute;width:240px}
.post .date{position:absolute;left:0;top:0;width:50px;height:50px;border-radius:50%;background:var(--smoke);border:1px solid var(--ash);color:var(--white);text-align:center;font-size:15px;font-weight:700;line-height:1;padding-top:10px}
.post .date small{display:block;font-size:10px;font-weight:400;margin-top:3px}
.post h3{margin-left:62px;font-size:16px;font-weight:600;color:var(--white);line-height:1.3}
.post p{margin-top:10px;font-size:12px;line-height:1.6;color:var(--muted)}
.post a{display:block;margin-top:8px;font-size:12px;color:var(--white);font-weight:600;text-decoration:none}
.social{left:0;top:1590px;width:1200px;height:610px;background:linear-gradient(180deg,#1b1b1b,#111)}
.card{position:absolute;top:20px;width:328px}
.card-head{height:50px;display:flex;align-items:center;padding-left:14px;gap:12px;font-family:"Rye",serif;font-size:26px;color:var(--white);text-transform:uppercase}
.card-head i{width:26px;height:26px;border-radius:50%;background:var(--white);display:block}
.card-body{height:440px;background:#f1f1f1;padding:14px;color:#333}
.fan .card-head{background:var(--fan)}
.tune .card-head{background:var(--tune)}
.snap .card-head{background:var(--snap)}
.fan-top{display:flex;gap:10px;align-items:center}
.avatar{width:48px;height:48px;background:linear-gradient(135deg,#8d8a87,#3c3a38)}
.fan-name{font-weight:700;font-size:14px;color:var(--fan)}
.fan-meta{font-size:11px;color:#777}
.fan-like{margin-top:4px;display:inline-block;border:1px solid #bbb;font-size:10px;padding:2px 6px;background:#fff}
.fan-post{margin-top:16px;font-size:11px;line-height:1.55;color:#444;border-top:1px solid #ddd;padding-top:12px}
.fan-post b{color:var(--fan)}
.fan-pic{margin-top:12px;height:120px;background:linear-gradient(135deg,#c9b8d9,#6b5b7c)}
.fan-friends{margin-top:14px;display:grid;grid-template-columns:repeat(6,1fr);gap:5px}
.fan-friends span{height:38px;background:linear-gradient(135deg,#a59f9a,#4a4642)}
.track{display:flex;gap:10px;align-items:center;height:70px;border-bottom:1px solid #d8d8d8}
.track .thumb{width:52px;height:52px;background:linear-gradient(135deg,#c6d4e6,#56708f);flex:none}
.track .wave{flex:1}
.track .wave div{font-size:10px;color:#555;margin-bottom:5px}
.track .wave svg{display:block}
.snap-grid{display:grid;grid-template-columns:repeat(3,1fr);gap:6px}
.snap-grid span{height:78px;display:block}
.follow{position:absolute;top:530px;border:2px solid var(--white);color:var(--white);font-size:12px;font-weight:700;padding:9px 16px;background:#000;text-transform:uppercase}
.sponsors{left:0;top:2200px;width:1200px;height:210px;background:var(--smoke)}
.sponsors .section-title{left:72px;top:20px;font-size:30px}
.badges{left:72px;top:94px;width:1056px;display:flex;justify-content:space-between}
.badges span{width:130px;height:70px;border-radius:8px;background:#2e2e2e;border:1px solid #3d3d3d}
.site-footer{left:0;top:2410px;width:1200px;height:274px;background:radial-gradient(ellipse at 50% 60%,#3a2e24,#0f0f0f 55%)}
.footer-figure{left:520px;top:20px;width:160px;height:254px;background:radial-gradient(ellipse at 50% 40%,#c79b62,#5c4328 50%,transparent 75%)}
.footer-col h4{font-size:14px;font-weight:700;color:var(--white);margin-bottom:12px}
.footer-col p,.footer-col li{font-size:11px;line-height:1.75;color:var(--muted);list-style:none}
.site-footer .social-dots{position:absolute;right:72px;top:40px}
.site-footer .logo{right:72px;top:88px;font-size:36px}
.copyright{right:72px;top:140px;font-size:11px;color:var(--muted)}
</style>
</head>
<body>

<header class="site-header abs">
  <div class="logo abs">Lirra</div>
  <div class="social-dots" aria-label="Social links"><span></span><span></span><span></span></div>
</header>

<nav class="main-nav abs">
  <a href="#">Home</a><a href="#">Events</a><a href="#">Upcoming Events &amp; Shows</a><a href="#">Book a Show</a><a href="#">Book a Maquillage</a><a href="#">Lirra on Social Media</a><a href="#">Sponsors &amp; Partners</a>
</nav>

<section class="hero abs">
  <div class="hero-left photo abs" role="img" aria-label="Portrait of Lirra Dusk in dramatic stage makeup"></div>
  <div class="hero-right photo abs" role="img" aria-label="Lirra Dusk posing in a silver costume against a pale blue backdrop"></div>
  <h1 class="hero-title abs">LIRRA</h1>
  <p class="hero-copy abs">Lirra Dusk is a young drag queen still going to college and living in the us.</p>
  <a class="btn" href="#">Book a Show</a>
  <svg class="slider-ctrl abs" width="60" height="24" viewBox="0 0 60 24" aria-label="Slider controls">
    <polyline points="16,4 8,12 16,20" fill="none" stroke="#fff" stroke-width="2"/>
    <polyline points="44,4 52,12 44,20" fill="none" stroke="#fff" stroke-width="2"/>
  </svg>
</section>

<section class="about abs">
  <h2 class="section-title abs">About Lirra</h2>
  <p class="about-copy abs">In publishing and graphic design, lorem ipsum is a filler text commonly used to demonstrate the graphic elements of a document or visual presentation. Replacing meaningful content with placeholder text allows viewers to focus on graphic aspects such as font, typography, and page layout without being distracted by the content. Replacing meaningful content with placeholder text allows viewers to focus on graphic aspects such as font, typography, and page layout without being distracted by the content.</p>
  <a class="btn" href="#">Book a Maquillage</a>
</section>
<div class="about-photo photo abs" role="img" aria-label="Lirra Dusk in a black hat and gothic makeup"></div>

<section class="feeds abs">
  <h2 class="section-title abs" style="left:72px">Upcoming Events and Shows</h2>
  <h2 class="section-title abs" style="left:612px">Latest Blog</h2>

  <div class="img-block photo" style="left:72px;top:70px;width:520px;height:200px;background:linear-gradient(120deg,#7ec4e8,#f0c4d6 50%,#4aa0d8)" role="img" aria-label="Event video: colourful parade show">
    <svg class="play abs" viewBox="0 0 64 64" aria-label="Play"><circle cx="32" cy="32" r="30" fill="#1f8fe0"/><polygon points="25,18 48,32 25,46" fill="#fff"/></svg>
  </div>
  <div class="img-block photo" style="left:72px;top:290px;width:250px;height:170px;background:linear-gradient(135deg,#a9d6ef,#4d87b9)" role="img" aria-label="Event photo: performer on a blue stage"></div>
  <div class="img-block photo" style="left:342px;top:290px;width:250px;height:170px;background:linear-gradient(135deg,#4aa3e0,#d5e5f2 55%,#c24f7e)" role="img" aria-label="Event photo: performer with blue hair"></div>

  <div class="img-block photo" style="left:612px;top:70px;width:246px;height:160px;background:linear-gradient(150deg,#3a2f22,#b89058 60%,#2a2118)" role="img" aria-label="Blog photo: golden gown on stage"></div>
  <div class="img-block photo" style="left:882px;top:70px;width:246px;height:160px;background:linear-gradient(120deg,#9fd1ec,#f2e7d6 50%,#6fb8dc)" role="img" aria-label="Blog photo: outdoor pride event"></div>

  <article class="post" style="left:612px;top:246px">
    <div class="date">08<small>Apr</small></div>
    <h3>Lorem ipsum dolor sit amet</h3>
    <p>Lorem ipsum dolor sit amet, consectetur adipiscing elit, sed do eiusmod tempor incididunt ut labore et dolore.</p>
    <a href="#">Read more ›</a>
  </article>
  <article class="post" style="left:882px;top:246px">
    <div class="date">08<small>Apr</small></div>
    <h3>Lorem ipsum dolor sit amet</h3>
    <p>Lorem ipsum dolor sit amet, consectetur adipiscing elit, sed do eiusmod tempor incididunt ut labore et dolore.</p>
    <a href="#">Read more ›</a>
  </article>
</section>

<section class="social abs">
  <div class="card fan" style="left:72px">
    <div class="card-head"><i></i>Fanpage</div>
    <div class="card-body">
      <div class="fan-top">
        <div class="avatar" role="img" aria-label="Profile photo"></div>
        <div><div class="fan-name">Lirra</div><div class="fan-meta">Performer · 1,204 likes</div><span class="fan-like">Like Page</span></div>
      </div>
      <div class="fan-post"><b>Lirra</b> Tonight we glow and getting ready for the big show downtown. Thanks to everyone who came out last weekend, see you all at the next stage night!</div>
      <div class="fan-pic" role="img" aria-label="Shared show photo"></div>
      <div class="fan-friends"><span></span><span></span><span></span><span></span><span></span><span></span><span></span><span></span><span></span><span></span><span></span><span></span></div>
    </div>
    <div class="follow" style="left:0">Follow Us</div>
  </div>

  <div class="card tune" style="left:436px">
    <div class="card-head"><i></i>Tunewave</div>
    <div class="card-body">
      <div class="track"><div class="thumb"></div><div class="wave"><div>Lirra – Midnight Glow</div><svg width="220" height="26"><rect width="220" height="26" fill="#ccc"/><rect width="80" height="26" fill="#f26f22"/></svg></div></div>
      <div class="track"><div class="thumb"></div><div class="wave"><div>Lirra – Velvet Stage</div><svg width="220" height="26"><rect width="220" height="26" fill="#ccc"/><rect width="40" height="26" fill="#f26f22"/></svg></div></div>
      <div class="track"><div class="thumb"></div><div class="wave"><div>Lirra – Silver Heels</div><svg width="220" height="26"><rect width="220" height="26" fill="#ccc"/></svg></div></div>
      <div class="track"><div class="thumb"></div><div class="wave"><div>Lirra – Neon Crown</div><svg width="220" height="26"><rect width="220" height="26" fill="#ccc"/></svg></div></div>
      <div class="track"><div class="thumb"></div><div class="wave"><div>Lirra – Last Encore</div><svg width="220" height="26"><rect width="220" height="26" fill="#ccc"/></svg></div></div>
      <div class="track" style="border:0"><div class="thumb"></div><div class="wave"><div>Lirra – Blue Hour</div><svg width="220" height="26"><rect width="220" height="26" fill="#ccc"/></svg></div></div>
    </div>
    <div class="follow" style="left:0">Follow Us</div>
  </div>

  <div class="card snap" style="left:800px">
    <div class="card-head"><i></i>Snapgrid</div>
    <div class="card-body" style="background:#1b1b1b">
      <div class="snap-grid" role="img" aria-label="Grid of recent show photos">
        <span style="background:linear-gradient(135deg,#7fb6e0,#2d5b86)"></span>
        <span style="background:linear-gradient(135deg,#d9c2e6,#6b449b)"></span>
        <span style="background:linear-gradient(135deg,#e8d2b0,#7a5a38)"></span>
        <span style="background:linear-gradient(135deg,#4aa0d8,#1b3a5c)"></span>
        <span style="background:linear-gradient(135deg,#c8c4c0,#3f3b38)"></span>
        <span style="background:linear-gradient(135deg,#d2a4cc,#5a3a6b)"></span>
        <span style="background:linear-gradient(135deg,#9ed0f0,#3a6f9a)"></span>
        <span style="background:linear-gradient(135deg,#b7a48a,#3a2e24)"></span>
        <span style="background:linear-gradient(135deg,#e4daeb,#8d78a6)"></span>
        <span style="background:linear-gradient(135deg,#6fa6d4,#233d58)"></span>
        <span style="background:linear-gradient(135deg,#c6b1d8,#4b3269)"></span>
        <span style="background:linear-gradient(135deg,#a8d0ea,#4d87b9)"></span>
        <span style="background:linear-gradient(135deg,#ddd,#555)"></span>
        <span style="background:linear-gradient(135deg,#8ec0e4,#2f5f8c)"></span>
        <span style="background:linear-gradient(135deg,#d9b88f,#5c4328)"></span>
      </div>
    </div>
    <div class="follow" style="left:0">Follow Us</div>
  </div>
</section>

<section class="sponsors abs">
  <h2 class="section-title abs">Sponsors and Partners</h2>
  <div class="badges abs" aria-label="Partner badges"><span></span><span></span><span></span><span></span><span></span><span></span></div>
</section>

<footer class="site-footer abs">
  <div class="footer-figure photo abs" role="img" aria-label="Lirra Dusk in a golden gown"></div>
  <div class="footer-col abs" style="left:72px;top:36px">
    <h4>Get In Touch</h4>
    <p>12 Ember Lane<br>Mesa Heights, 00000<br>United States<br><br>(000) 555-0142<br>lirra@lirradusk.example</p>
  </div>
  <div class="footer-col abs" style="left:300px;top:36px">
    <h4>Navigation</h4>
    <ul><li>Blog</li><li>Events</li><li>Upcoming Events &amp; Shows</li><li>Book a Show</li><li>Book a Maquillage</li><li>Lirra on Social Media</li><li>Sponsors &amp; Partners</li></ul>
  </div>
  <div class="social-dots" aria-label="Social links"><span></span><span></span><span></span></div>
  <div class="logo abs">Lirra</div>
  <p class="copyright abs">© 2015 Lirra Dusk. All Rights Reserved.</p>
</footer>

</body>
</html>
```